CG 1 page flyer

I need a flyer design for a financial risk advisory business. I like the layout of the example on your site, for Delia Fenwick (attached). Our business needs to show strength, safety, knowledge and security. We provide financial advice.

I have uploaded the front page of our larger brochure. I would like the man with the umbrella with the caption and the logo / brand on the front page, but with portrait orientation, instead of landscape.

For the second page (the back), I have got some ideas of the kinds of things I would want written on the attached Power Point. But it needs to be arranged better, with perhaps the Corvin's Gate Logo on there as well, to break up all the writing. Attached is an example of how it might look, but I want different formatting and layout ideas, that look better, more professional etc.

The page 1 comment what is corvins gate? predicting ......... would look better all the way along the bottom of the page, but i couldn't get the formatting right.

```html
<!DOCTYPE html>
<html lang="en">
<head>
<meta charset="utf-8">
<title>Corvin's Gate – Financial Risk Advisory Flyer</title>
<link href="https://fonts.googleapis.com/css2?family=Open+Sans:ital,wght@0,300;0,400;0,600;0,700;1,400;1,600;1,700;1,800&display=swap" rel="stylesheet">
<style>
  :root{
    --stage:#000000;
    --navy:#232a63;
    --navy-deep:#1b2155;
    --sky:#1fa6e6;
    --sky-light:#3cb8f0;
    --white:#ffffff;
    --grey-top:#d4d4d6;
    --grey-bottom:#b3b3b6;
    --ink:#1d1d1f;
  }
  *{box-sizing:border-box;margin:0;padding:0}
  html,body{width:876px;height:1200px;overflow:hidden;background:var(--stage)}
  body{position:relative;font-family:"Open Sans",Arial,sans-serif}

  .page{position:absolute;top:32px;width:392px;height:530px;overflow:hidden}
  .page--front{left:30px;background:var(--white)}
  .page--back{left:452px;background:var(--white)}

  /* brand lockup */
  .brand{position:absolute;display:flex;flex-direction:column}
  .brand__row{display:flex;align-items:center;gap:6px}
  .brand__name{font-weight:700;color:var(--navy);font-size:25px;letter-spacing:-.3px;line-height:1;white-space:nowrap}
  .brand__dot{width:14px;height:14px;border-radius:50%;background:var(--sky)}
  .brand__tagline{font-size:8.5px;color:var(--sky);margin-top:3px;word-spacing:5px;white-space:nowrap}

  /* front */
  .front__slogan{position:absolute;left:234px;top:27px;color:var(--sky);font-weight:700;font-size:12.5px;line-height:14px;white-space:nowrap}
  .front__hero{position:absolute;left:0;top:151px;width:392px;height:268px;
    background:radial-gradient(ellipse at 78% 45%,#2f86d3 0%,#1d4f9e 35%,var(--navy-deep) 75%)}
  .front__photo{position:absolute;left:195px;top:0;width:197px;height:268px;
    background:linear-gradient(180deg,rgba(30,30,40,0) 0%,rgba(40,40,52,.35) 40%,rgba(35,35,45,.55) 100%)}
  .front__title{position:absolute;left:42px;top:63px;color:var(--sky-light);font-weight:800;font-style:italic;font-size:27px;line-height:32px;letter-spacing:-.5px;white-space:nowrap}
  .services{position:absolute;left:48px;top:150px;list-style:none}
  .services li{display:flex;align-items:center;gap:8px;height:35px;color:var(--white);font-style:italic;font-size:12.5px;white-space:nowrap}
  .services svg{width:26px;height:22px;flex:none}
  .front__footer{position:absolute;left:0;top:419px;width:392px;height:111px;
    border-top:3px solid var(--white);background:linear-gradient(180deg,var(--grey-top),var(--grey-bottom))}
  .front__question{position:absolute;left:168px;top:22px;font-size:16.5px;color:var(--ink);white-space:nowrap}
  .front__quote{position:absolute;left:168px;top:47px;font-size:12px;font-weight:700;line-height:14px;color:var(--ink);white-space:nowrap}

  /* back */
  .back__panel{position:absolute;left:0;top:0;width:392px;height:426px;background:var(--navy)}
  .back__headline{position:absolute;left:36px;top:50px;color:var(--sky);font-weight:300;font-size:16.5px;line-height:21px;white-space:nowrap}
  .col{position:absolute;color:var(--white);font-size:7px;line-height:10.6px;letter-spacing:-.1px}
  .col--left{left:36px;top:150px;width:152px}
  .col--right{left:203px;top:50px;width:168px}
  .col h3{color:var(--sky);font-style:italic;font-weight:700;font-size:7px;text-transform:uppercase;margin-top:7px}
  .col h3.plain{text-transform:none}
  .col h3:first-child{margin-top:0}
  .col p + p{margin-top:10px}
  .checklist{list-style:none;margin-top:2px}
  .checklist li{font-weight:700;position:relative;padding-left:10px}
  .checklist li::before{content:"";position:absolute;left:1px;top:2.5px;border-left:5px solid var(--sky);border-top:3px solid transparent;border-bottom:3px solid transparent}
  .back__closing{position:absolute;left:36px;top:442px;color:var(--navy);font-style:italic;font-size:12px;line-height:19px;white-space:nowrap}
</style>
</head>
<body>

<section class="page page--front" aria-label="Flyer front">
  <div class="brand" style="left:42px;top:38px">
    <div class="brand__row"><span class="brand__name">Corvin's Gate</span><span class="brand__dot"></span></div>
    <span class="brand__tagline">Our experience Your edge</span>
  </div>
  <p class="front__slogan">Whatever the<br>Financial Forecast...<br>It pays to be prepared!</p>

  <div class="front__hero">
    <div class="front__photo" role="img" aria-label="Photograph of a man in a dark suit and bowler hat seated, holding an open black umbrella"></div>
    <h1 class="front__title">Financial<br>Risk Advisory</h1>
    <ul class="services">
      <li><svg viewBox="0 0 26 22" aria-hidden="true"><rect x="4" y="3" width="20" height="12" fill="none" stroke="#fff" stroke-width="1.4"/><rect x="1" y="7" width="20" height="12" fill="#1d4f9e" stroke="#fff" stroke-width="1.4"/><circle cx="11" cy="13" r="3" fill="none" stroke="#fff" stroke-width="1.2"/></svg>Debt &amp; Funding</li>
      <li><svg viewBox="0 0 26 22" aria-hidden="true"><path d="M11 1 L21 20 H1 Z" fill="#fff"/><rect x="10" y="7" width="2" height="7" fill="#1d2560"/><rect x="10" y="16" width="2" height="2" fill="#1d2560"/><circle cx="20" cy="8" r="5" fill="#fff" stroke="#1d2560" stroke-width="1"/><path d="M17.5 8 L19.5 10 L22.5 6" fill="none" stroke="#1d2560" stroke-width="1.5"/></svg>Market Risk</li>
      <li><svg viewBox="0 0 26 22" aria-hidden="true"><circle cx="7" cy="12" r="4" fill="none" stroke="#fff" stroke-width="1.4" stroke-dasharray="2 1.4"/><circle cx="16" cy="5" r="3.2" fill="none" stroke="#fff" stroke-width="1.4"/><path d="M11 21 V12 Q16 8 21 12 V21" fill="none" stroke="#fff" stroke-width="1.4"/></svg>Active Engagement</li>
    </ul>
  </div>

  <div class="front__footer">
    <p class="front__question">What is Corvin's Gate?</p>
    <p class="front__quote">Predicting rain doesn’t count;<br>building arks does”</p>
  </div>
</section>

<section class="page page--back" aria-label="Flyer back">
  <div class="back__panel">
    <h2 class="back__headline">You can't Outsource<br>your Risk,<br>but you can<br>Insource Expertise</h2>

    <div class="col col--left">
      <h3>Who is Corvin's Gate?</h3>
      <p>A team of independent, passionate risk advisors with over 200 years combined experience in financial market risk management, funding &amp; debt advisory.</p>
      <h3>What can we do for you?</h3>
      <p>We partner with clients to gain a deep understanding of their needs. We then help them solve their risk and funding issues by creating and explaining sustainable treasury policy.</p>
      <h3 class="plain">Debt Advisory</h3>
      <p>Design &amp; Execution of debt funding strategies.<br>Market Risk Advisory<br>Design &amp; Execution of hedging strategies<br>Active Engagement<br>Fully engaged risk review, reporting, strategy development and execution enhancement.</p>
      <h3>What is our measure of success?</h3>
      <p>Our only true measure of success is successful, sustainable clients that stand out from their peers.</p>
    </div>

    <div class="col col--right">
      <h3>What it means for our clients</h3>
      <p>Our market experience means our clients receive well considered, completely independent advice and solutions covering:</p>
      <ul class="checklist">
        <li>Commodities</li>
        <li>Foreign Exchange</li>
        <li>Interest Rates</li>
        <li>Project Finance</li>
        <li>Treasury Software Solutions</li>
        <li>Market Valuations incl. CVA / DVA</li>
        <li>Hedge Effectiveness Testing</li>
        <li>Compliance Reporting</li>
      </ul>
      <h3>Our principles</h3>
      <p>Aspire to always deliver value to our clients.<br>Always provide frank, robust advice.<br>Be fierce but commercial client advocates.</p>
      <h3>What's our philosophy?</h3>
      <p>Markets are dynamic, so proper Risk Management must also be a dynamic and on-going process. Risk Management is not about “beating the market”, its about “not taking a beating” from adverse market conditions.</p>
      <p>When your bottom line is exposed to volatile markets, appropriate preparation is the key to a sustainable business. We help our clients to integrate their risk management objectives with their overall corporate strategy.</p>
    </div>
  </div>

  <p class="back__closing">Integration of Market<br>Risk Strategy &amp; Corporate<br>Strategy is Essential</p>
  <div class="brand" style="left:224px;top:472px">
    <div class="brand__row"><span class="brand__name" style="font-size:21px">Corvin's Gate</span><span class="brand__dot" style="width:12px;height:12px"></span></div>
    <span class="brand__tagline">Our experience Your edge</span>
  </div>
</section>

</body>
</html>
```